Business card New design- upscale

Looking for modern design business cards. Minimalist, mix of gloss and matte finishes. Texas based Contractor company doing Mechanical hvac and plumbing, focused on commercial and industrial manufacturing facilities. We don't hand too many out so high end materials or functionality...will be considered. Please see attached files for info needed on cards. *New plumbing license needs to be edited to say M82716. Www.polvaxgroup.com
P.s. Website will also be redesigned soon.

Target Market(s)

Facility managers for commercial buildings, mechanical engineers for industrial manufacturing facilities including pharmaceutical, semiconductor, food & beverage, etc

Contact Information for Business Card

See attached images

Requirements
Must have
• All Logo colors: purple, black and Gray. 1, 2 or 4 rounded corners. All content on existing business cards (see attached images).
Nice to have
• Matte and gloss print. Embossing, raised print, functionality.
Should not have
• Stock images, generic construction.

```html
<!DOCTYPE html>
<html lang="en">
<head>
<meta charset="utf-8">
<title>Polvax Group — Business Card</title>
<link href="https://fonts.googleapis.com/css2?family=Noto+Sans:wght@400;700&display=swap" rel="stylesheet">
<style>
  :root {
    --backdrop: #93969b;
    --purple: #3d2763;
    --purple-deep: #2f1c52;
    --paper: #ececec;
    --ink-grey: #5e5e62;
    --white: #ffffff;
  }
  * { margin: 0; padding: 0; box-sizing: border-box; }
  html, body {
    width: 1200px; height: 900px; overflow: hidden;
    background: var(--backdrop);
    font-family: "Noto Sans", sans-serif;
  }
  .stage { position: relative; width: 1200px; height: 900px; }
  .card {
    position: absolute; top: 214px;
    width: 270px; height: 474px;
    border-radius: 24px; overflow: hidden;
    text-align: center;
  }
  .card--back { left: 288px; background: var(--purple); color: var(--white); }
  .card--front { left: 641px; background: var(--paper); color: var(--ink-grey); }

  .brand {
    position: absolute; left: 0; right: 0;
    display: flex; align-items: center; justify-content: center; gap: 8px;
  }
  .brand__mark { width: 16px; height: 16px; }
  .brand__name { font-size: 26px; font-weight: 700; letter-spacing: 1px; line-height: 1; }
  .card--back .brand { top: 78px; }
  .card--back .brand__mark { background: var(--purple-deep); }
  .card--back .brand__name { color: var(--purple-deep); }
  .card--front .brand { top: 90px; }
  .card--front .brand__mark { background: var(--purple); }
  .card--front .brand__name { color: var(--purple); }

  .license {
    position: absolute; left: 0; right: 0;
    font-size: 11.5px; line-height: 15.1px;
  }
  .license--plumbing { top: 157px; }
  .license--tdlr { top: 325px; }

  .person { position: absolute; top: 206px; left: 0; right: 0; }
  .person__name { font-size: 13.5px; font-weight: 700; color: var(--purple); letter-spacing: .3px; line-height: 18px; }
  .person__title { font-size: 11.5px; line-height: 16px; }

  .address { position: absolute; top: 288px; left: 0; right: 0; font-size: 11.5px; line-height: 15.1px; }

  .contact-icons {
    position: absolute; top: 326px; left: 0; right: 0;
    display: flex; justify-content: center; gap: 3px;
  }
  .contact-icons svg { width: 16px; height: 16px; }

  .contacts { position: absolute; top: 350px; left: 0; right: 0; font-size: 11.5px; line-height: 15.1px; }
  .contacts__site-name { color: var(--purple); }

  .services-band {
    position: absolute; left: 0; right: 0; bottom: 0; height: 47px;
    background: var(--purple); color: var(--white);
    font-size: 11.5px; line-height: 15px;
    display: flex; flex-direction: column; justify-content: center;
  }
</style>
</head>
<body>
<main class="stage">

  <section class="card card--back">
    <div class="brand">
      <span class="brand__mark"></span>
      <span class="brand__name">POLVAX GROUP</span>
    </div>
    <p class="license license--plumbing">
      RMP-M82716<br>
      Regulated by the<br>
      Texas State Board of<br>
      Plumbing Examiners,<br>
      P.O. Box 3100,<br>
      Austin, TX. 78765;<br>
      1-800-555-0148,<br>
      512-555-0172/ TACLA58203C
    </p>
    <p class="license license--tdlr">
      Regulated by the<br>
      Texas Department of<br>
      Licensing and Regulation,<br>
      P.O. Box 10480,<br>
      Austin, TX. 78711;<br>
      1-800-555-0193,<br>
      512-555-0126<br>
      www.txlicensing.example.org
    </p>
  </section>

  <section class="card card--front">
    <div class="brand">
      <span class="brand__mark"></span>
      <span class="brand__name">POLVAX GROUP</span>
    </div>

    <div class="person">
      <p class="person__name">DALE MORENO</p>
      <p class="person__title">Lead Estimator/Sr. Project Manager</p>
    </div>

    <p class="address">2180 Cedar Mill Rd.<br>Fort Worth, TX 76140</p>

    <div class="contact-icons">
      <svg viewBox="0 0 16 16" aria-label="Mobile"><circle cx="8" cy="8" r="8" fill="#3d2763"/><rect x="5.5" y="3.5" width="5" height="9" rx="1" fill="none" stroke="#fff" stroke-width="1.1"/><circle cx="8" cy="11" r=".6" fill="#fff"/></svg>
      <svg viewBox="0 0 16 16" aria-label="Phone"><circle cx="8" cy="8" r="8" fill="#3d2763"/><path d="M5 4.2l1.6-.4 1 2.2-1 .8a6 6 0 0 0 2.6 2.6l.8-1 2.2 1-.4 1.6c-3.6.3-7-3.2-6.8-6.8z" fill="#fff"/></svg>
      <svg viewBox="0 0 16 16" aria-label="Email"><circle cx="8" cy="8" r="8" fill="#3d2763"/><rect x="4" y="5" width="8" height="6" rx=".6" fill="#fff"/><path d="M4.3 5.4L8 8.4l3.7-3" fill="none" stroke="#3d2763" stroke-width=".9"/></svg>
      <svg viewBox="0 0 16 16" aria-label="Website"><circle cx="8" cy="8" r="8" fill="#3d2763"/><g fill="none" stroke="#fff" stroke-width=".9"><circle cx="8" cy="8" r="4.2"/><ellipse cx="8" cy="8" rx="1.8" ry="4.2"/><path d="M3.8 8h8.4M4.5 5.8h7M4.5 10.2h7"/></g></svg>
    </div>

    <p class="contacts">
      (520) 555-0143<br>
      (817) 555-0187<br>
      dmoreno@polvaxgroup.com<br>
      www.<span class="contacts__site-name">polvaxgroup</span>.com
    </p>

    <div class="services-band">
      <p>Commercial &amp; Industrial Contactors</p>
      <p>Mechanical &amp; Plumbing Services</p>
    </div>
  </section>

</main>
</body>
</html>
```